Business and Success Coaching Business Card

Need a business card for my coaching business. I coach small businesses, career professionals and, individuals wanting to unlock their human potential and achieve excellence. At the heart of our methodology is the Shaping Purposeful Action Routines Knowingly (SPARK) approach to formulate empowerment, create principles for success and setting achievable outcomes. I would like something that incorporates our new logo, something clean and sharp with a solid darker, but complementary background, color on the card front. The back should be white where there will be room for three questions

Target Market(s)

People looking to advance and improve themselves through a success coach

Industry/Entity Type

Life Coaching

Contact Information for Business Card

Contact information on card.
Business name on front of card
Questions on back

Font styles to use
Other font styles liked:
• Century Gothic or other Serif style fonts that look similar to Century Gothic

Colors

Designer to choose colors to be used in the design.

Requirements
Must have
• Logo on front of card
• Business name - The Steady Forge
• Contact name - Ted Harlow
• Address - Box 4619, Littleton, CO 80127-4619
• Phone number - 303-555-0147
• Email address - harlow.ted@thesteadyforge.example
• Certifications - CSC, CCHt, PTT, PNLP
• Back of card
• Three questions on the back of the card:
• If you were at your best, what would you do right now?
• What is the decision you have been avoiding?
• What's one action you could take in the next 10 minutes?
Nice to have
• I would like to see a solid color on the front of the card that compliments the logo.
• Back should be white, or could be contrasting, but need to have the three questions.

```html
<!DOCTYPE html>
<html lang="en">
<head>
<meta charset="utf-8">
<title>The Steady Forge – Card Back</title>
<link rel="stylesheet" href="https://fonts.googleapis.com/css2?family=Questrial&display=swap">
<style>
  :root {
    --card-bg: #ffffff;
    --ink: #1a1a1a;
  }
  html, body {
    margin: 0;
    padding: 0;
    overflow: hidden;
    background: var(--card-bg);
  }
  .card-back {
    position: relative;
    width: 683px;
    height: 1200px;
    background: var(--card-bg);
    color: var(--ink);
    font-family: "Questrial", "Century Gothic", sans-serif;
    overflow: hidden;
  }
  .question {
    position: absolute;
    left: 0;
    width: 683px;
    margin: 0;
    text-align: center;
    font-size: 33px;
    font-weight: 400;
    line-height: 43px;
    letter-spacing: 0.2px;
  }
  .question--best { top: 345px; left: -13px; }
  .question--decision { top: 557px; left: -8px; }
  .question--action { top: 770px; left: -13px; }
</style>
</head>
<body>
  <main class="card-back">
    <p class="question question--best">If you were at your best,<br>what would you do right now?</p>
    <p class="question question--decision">What is the decision you have<br>been avoiding?</p>
    <p class="question question--action">What’s one action you could<br>take in the next 10 minutes?</p>
  </main>
</body>
</html>
```